Brochure & Business card design

Looking for a new business card design i want it to be modern and sharp looking i usually order plastic business cards, and i would like to make the colors like the logo teal/charcoal i will like to have our services on icons with words.... our services are
ROOFING GUTTERS PAINTING PRESSURE WASHING EXTERIOR DESIGN & ATTIC VENTILATION. I also want to add my credentials

Target Market(s)

Oregon local market

Industry/Entity Type

Residential Construction

Contact Information for Business Card

Business info, services, number, website

Font styles to use
Serif
Sans Serif

Colors
33b8a4
5c5c5c
ffffff

Requirements
Must have
• Dale Finch
• Cell:
• Office:
• Email:
• Website:
• also i need our social media icons
• Services ROOFING GUTTERS PAINTING PRESSURE WASHING EXTERIOR DESIGN & ATTIC VENTILATION
• -icons for number, web, email, cell
• OR #584312
• Wa #KTRABLD461X7
Nice to have
• -Clean design Front & Back
• -Icons
• -shape House just like logo design
• -First Impression
Should not have
• Not Busy or lost of eye contact

```html
<!DOCTYPE html>
<html lang="en">
<head>
<meta charset="utf-8">
<title>Ridgeline Co. – Business Card</title>
<link href="https://fonts.googleapis.com/css2?family=Merriweather:wght@400;700;900&family=Montserrat:wght@400;500&display=swap" rel="stylesheet">
<style>
  :root{
    --teal:#1c9686;
    --teal-bright:#33b8a4;
    --charcoal:#5c5c5c;
    --charcoal-dark:#4a4a4c;
    --white:#ffffff;
    --ink:#222222;
    --stage:#3a3a3c;
    --social:#3a6fb0;
  }
  *{box-sizing:border-box;margin:0;padding:0}
  html,body{width:1200px;height:782px;overflow:hidden;background:var(--stage)}
  .canvas{position:relative;width:1200px;height:782px}

  .card{position:absolute;width:600px;height:340px;overflow:hidden;box-shadow:0 10px 30px rgba(0,0,0,.35)}

  /* Back card */
  .card-back{left:540px;top:50px;background:var(--teal)}
  .card-back .base-band{position:absolute;left:0;right:0;bottom:0;height:115px;background:var(--charcoal-dark)}
  .brand{display:flex;align-items:center;gap:12px;font-family:'Merriweather',serif;font-weight:900;font-size:28px;line-height:1.1;white-space:nowrap}
  .brand-mark{flex:none;width:18px;height:18px;background:currentColor}
  .card-back .brand{position:absolute;left:50px;top:112px;color:var(--white)}
  .card-back .cert-badge{position:absolute;left:70px;top:228px;width:120px;height:44px;background:var(--white);border:3px solid var(--teal)}
  .card-back .divider{position:absolute;left:320px;top:40px;width:1px;height:170px;background:rgba(255,255,255,.45)}
  .services{position:absolute;left:345px;top:58px;list-style:none;color:var(--white);font-family:'Montserrat',sans-serif;font-size:15px;letter-spacing:.5px;line-height:21px}
  .services li{display:flex;align-items:center;gap:8px}
  .services li::before{content:"";width:6px;height:6px;border-radius:50%;background:var(--white)}
  .card-back .accredit-frame{position:absolute;left:345px;top:226px;width:150px;height:56px;background:var(--teal);padding:6px}
  .accredit-frame .accredit-badge{width:100%;height:100%;background:#111}

  /* Front card */
  .card-front{left:70px;top:390px;background:var(--white)}
  .holder-name{position:absolute;left:70px;top:40px;font-family:'Merriweather',serif;font-weight:900;font-size:20px;letter-spacing:.5px;color:var(--charcoal)}
  .holder-name .first{color:var(--teal)}
  .contacts{position:absolute;left:70px;top:140px;list-style:none;font-family:'Merriweather',serif;font-size:14px;line-height:21px;color:var(--ink)}
  .contacts li{display:flex;align-items:center;gap:8px}
  .contacts svg{width:12px;height:12px;fill:var(--teal);flex:none}
  .contacts .licenses{color:var(--teal);margin-top:2px}
  .card-front .brand{position:absolute;left:360px;top:150px;color:var(--teal)}
  .front-bands{position:absolute;left:0;bottom:0;width:600px;height:90px}
  .socials{position:absolute;right:40px;bottom:16px;display:flex;gap:6px}
  .socials span{width:26px;height:26px;border-radius:50%;background:var(--social);border:2px solid var(--white)}
</style>
</head>
<body>
<main class="canvas">

  <section class="card card-back" aria-label="Card back">
    <div class="base-band"></div>
    <div class="brand"><span class="brand-mark"></span><span>Ridgeline Co.</span></div>
    <div class="cert-badge" role="img" aria-label="Manufacturer certification badge"></div>
    <div class="divider"></div>
    <ul class="services">
      <li>ROOFING</li>
      <li>GUTTERS</li>
      <li>PAINTING</li>
      <li>PRESSURE WASHING</li>
      <li>EXTERIOR DESIGN &amp;</li>
      <li>ATTIC VENTILATION</li>
    </ul>
    <div class="accredit-frame"><div class="accredit-badge" role="img" aria-label="Business accreditation badge"></div></div>
  </section>

  <section class="card card-front" aria-label="Card front">
    <h1 class="holder-name"><span class="first">DALE</span> FINCH</h1>
    <ul class="contacts">
      <li><svg viewBox="0 0 24 24"><path d="M6.6 10.8a15 15 0 0 0 6.6 6.6l2.2-2.2a1 1 0 0 1 1-.25 11.4 11.4 0 0 0 3.6.57 1 1 0 0 1 1 1V20a1 1 0 0 1-1 1A17 17 0 0 1 3 4a1 1 0 0 1 1-1h3.5a1 1 0 0 1 1 1c0 1.25.2 2.45.57 3.57a1 1 0 0 1-.25 1z"/></svg>503-555 0148</li>
      <li><svg viewBox="0 0 24 24"><path d="M7 1h10a2 2 0 0 1 2 2v18a2 2 0 0 1-2 2H7a2 2 0 0 1-2-2V3a2 2 0 0 1 2-2zm0 3v14h10V4z"/></svg>503-555 0172</li>
      <li><svg viewBox="0 0 24 24"><path d="M2 5h20v14H2zm2 2v.5l8 5 8-5V7z"/></svg>info@ridgelineco.com</li>
      <li><svg viewBox="0 0 24 24"><circle cx="12" cy="12" r="10"/></svg>www.ridgelineco.com</li>
      <li class="licenses">OR #584312 | Wa #KTRABLD461X7</li>
    </ul>
    <div class="brand"><span class="brand-mark"></span><span>Ridgeline Co.</span></div>
    <svg class="front-bands" viewBox="0 0 600 90" preserveAspectRatio="none" aria-hidden="true">
      <polygon points="0,40 300,70 300,90 0,90" fill="#5c5c5c"/>
      <polygon points="300,40 600,70 600,90 280,90" fill="#1c9686"/>
    </svg>
    <div class="socials" aria-label="Social media links"><span></span><span></span><span></span><span></span></div>
  </section>

</main>
</body>
</html>
```